Two documents one design language.

We are a small insurance broker who is committed to being open and transparent as possible with our customers.

For years, we have used plain word documents (see attachments) for our Policy Wording and our Terms of Business.

But now think we can do better and these plain documents are falling behind what our competitors are offering.

So we are now looking for both these documents to be professionally designed using the same design language for both.

We are putting few constraints on the design, but we do have some:
- It must be done in word as the wording can be changed at any time, so we must be able to maintain the documents ourselves.
- Any pictures or graphics you use must be royalty free so we can re-produce with any complications.
- Any pictures or graphics you use must been supplied as part of the package.
- You MUST NOT change any wording or grammar, it's not ours to change, its the insurers wording and HAS to be agreed with them.
- You must not split any any paragraph or bullet point over two pages.
- We are an insurance broker so what ever design you use, must look professional and inspire confidence... I.e. if you read it your thoughts turn to, these people are approachable, know what they are doing and will look after me.
- We specialise in musical instrument insurance, so we are looking for musical theming.

```html
<!DOCTYPE html>
<html lang="en">
<head>
<meta charset="utf-8">
<title>Harlow Reed Insurance – Policy Wording</title>
<link rel="stylesheet" href="https://fonts.googleapis.com/css2?family=Montserrat:wght@800&family=Arimo:wght@400;700&display=swap">
<style>
  :root {
    --backdrop: #dcc8ca;
    --paper: #fbfafb;
    --paper-shade: #f1eef0;
    --plum: #5a3b68;
    --rose: #e27aa3;
    --rose-light: #f1abc6;
    --ink: #3c3a3d;
    --rule: #8a8789;
  }
  * { box-sizing: border-box; margin: 0; padding: 0; }
  html, body { width: 1200px; height: 800px; overflow: hidden; }
  body {
    background: var(--backdrop);
    font-family: "Arimo", Arial, sans-serif;
    color: var(--ink);
    position: relative;
  }
  .page {
    position: absolute;
    background: var(--paper);
    box-shadow: 0 6px 18px rgba(80, 50, 60, 0.18);
    overflow: hidden;
  }

  /* Front cover */
  .cover { left: 60px; top: 180px; width: 310px; height: 438px; }
  .cover__brand {
    position: absolute; top: 74px; left: 0; right: 0;
    display: flex; align-items: center; justify-content: center; gap: 8px;
  }
  .cover__brand-dot { width: 10px; height: 10px; border-radius: 50%; background: var(--rose); }
  .cover__brand-name {
    font-family: "Montserrat", Arial, sans-serif; font-weight: 800;
    font-size: 17px; color: var(--plum); letter-spacing: 0.5px;
  }
  .cover__art {
    position: absolute; left: 62px; top: 140px; width: 190px; height: 250px;
    background: radial-gradient(ellipse at 50% 50%, var(--rose-light) 0%, #f6d3e0 60%, var(--paper) 100%);
    border-radius: 6px;
  }

  /* Spread */
  .spread-left { left: 430px; top: 150px; width: 355px; height: 495px; padding: 22px 20px; }
  .spread-right { left: 785px; top: 150px; width: 355px; height: 495px; }
  .gutter {
    position: absolute; left: 775px; top: 150px; width: 20px; height: 495px;
    background: linear-gradient(90deg, transparent, rgba(0,0,0,0.08) 50%, transparent);
  }

  .heading { position: relative; font-family: "Montserrat", Arial, sans-serif; font-weight: 800; line-height: 1; }
  .heading__top { display: block; color: var(--plum); font-size: 26px; }
  .heading__band {
    display: block; margin-top: 3px; padding: 3px 10px;
    background: var(--rose); color: #fff; font-size: 26px;
  }
  .cover-provided .heading__band { margin-left: -20px; margin-right: -60px; padding-left: 20px; }

  .intro { font-size: 6.4px; line-height: 1.35; margin: 12px 0 8px; text-align: justify; }

  .cover-table { width: 100%; border-collapse: collapse; font-size: 5.9px; line-height: 1.28; }
  .cover-table th {
    font-weight: 700; font-size: 7.2px; text-align: left; padding: 2px 4px;
    border-bottom: 0.6px solid var(--rule);
  }
  .cover-table td { padding: 2px 4px; vertical-align: top; border-bottom: 0.6px solid var(--rule); }
  .cover-table td:first-child, .cover-table th:first-child { width: 22%; border-right: 0.6px solid var(--rule); }

  .footnote { position: absolute; bottom: 14px; left: 20px; right: 20px; font-size: 4.6px; color: var(--ink); }

  .extension { position: absolute; top: 44px; left: 128px; right: 0; }
  .extension .heading__band { margin-left: 10px; padding-left: 14px; }

  .extension-list {
    position: absolute; top: 128px; left: 176px; right: 20px;
    list-style: none; font-size: 6.6px; line-height: 1.35; text-align: justify;
  }
  .extension-list li { margin-bottom: 12px; }

  .model-photo {
    position: absolute; left: 20px; top: 120px; width: 150px; height: 375px;
    background: linear-gradient(180deg, #f3e7e4 0%, #efe9ea 35%, #e79ac0 60%, #8ea6c8 85%, #2e2c30 100%);
    border-radius: 4px 4px 0 0;
  }
</style>
</head>
<body>

  <section class="page cover">
    <div class="cover__brand">
      <span class="cover__brand-dot"></span>
      <span class="cover__brand-name">HARLOW REED INSURANCE</span>
    </div>
    <div class="cover__art" role="img" aria-label="Line illustration of a cherub playing a harp in pink"></div>
  </section>

  <section class="page spread-left">
    <h1 class="heading cover-provided">
      <span class="heading__top">THE COVER</span>
      <span class="heading__band">PROVIDED</span>
    </h1>
    <p class="intro">In return for payment of the premium shown in the SCHEDULE, this insurance covers the PROPERTY INSURED described in the SCHEDULE against accidental physical loss or damage caused during YOUR or a FRIEND use occurring during the PERIOD OF INSURANCE up to the respective sums insured and in accordance with the level of cover selected (Cover levels detailed below), all of which are shown in the SCHEDULE, subject to the terms, exclusions and conditions as detailed in this policy document.</p>
    <table class="cover-table">
      <thead>
        <tr><th>Level of Cover</th><th>Description of Cover</th></tr>
      </thead>
      <tbody>
        <tr><td>In-Home</td><td>Cover is only provided in YOUR home or in a single identified residential location.</td></tr>
        <tr><td>Student</td><td>Cover while YOU learn to play. YOUR instrument is covered in YOUR home and within UK/Ireland when attending a lesson with YOUR TEACHER or a prearranged concert/rehearsal at the request of YOUR TEACHER, to help extend YOUR learning to include performance.</td></tr>
        <tr><td>UK/Ireland</td><td>Cover in YOUR home, the UK and the Republic of Ireland</td></tr>
        <tr><td>Europe</td><td>Cover in YOUR home, the UK and any European country</td></tr>
        <tr><td>Worldwide</td><td>Cover in YOUR home and in any country in the world</td></tr>
        <tr><td>Retail</td><td>For retail customers, cover provided in YOUR retail PREMISES including transportation across the UK for display/demonstration at exhibitions.</td></tr>
        <tr><td>On Loan/Hire</td><td>If YOU hire YOUR instrument to a third party YOU can upgrade YOUR cover to include the risks presented by them looking after YOUR instrument, including theft of YOUR instrument.*</td></tr>
        <tr><td>Education</td><td>If YOU are a school, college or university, YOUR instrument is covered whilst on YOUR PREMISES and at any concert venue where YOU have booked a rehearsal or performance.</td></tr>
        <tr><td>Storage UK</td><td>If YOU need to store your instruments away from YOUR PREMISES in a professional storage unit, i.e. if you are having some building work done at home. The instruments need to be stored in a unit that has a secure entry, YOUR unit needs to be locked at all time YOU are not in attendance and the facility has to be staffed during normal office hours and monitored 24x7. NOTE: The instruments are not covered if they are removed from the storage unit.</td></tr>
        <tr><td>In Establishment</td><td>If YOU are a band or a group or similar and have your own separate building where you practice and store your instruments. NOTE: If your instruments are not covered if they are removed from the building.</td></tr>
      </tbody>
    </table>
    <p class="footnote">*Reasonable precautions apply to ensure you have: required evidence of the identity of the person who is loaning/hiring YOUR instrument.</p>
  </section>

  <section class="page spread-right">
    <h2 class="heading extension">
      <span class="heading__top">EXTENSION</span>
      <span class="heading__band">TO COVER</span>
    </h2>
    <div class="model-photo" role="img" aria-label="Photograph of a young musician seated on a stool holding a pink ukulele"></div>
    <ol class="extension-list">
      <li>1. Should the PROPERTY INSURED become damaged and WE accept that there is a valid claim WE will pay the cost of transporting the damaged item to/from the repairers – up to a maximum amount of £3,500.</li>
      <li>2. Should the PROPERTY INSURED become damaged and unplayable and WE accept that there is a valid claim WE will pay the cost of hiring a replacement instrument whilst it is being repaired or replaced - up to a maximum amount of £4,000.</li>
      <li>3. Where so noted on the above SCHEDULE with the words ‘Structure Cover’, WE will cover loss or damage to the related instrument caused by the failure of materials or workmanship, providing the damage becomes apparent to the naked eye during the PERIOD OF INSURANCE.</li>
    </ol>
  </section>

  <div class="gutter"></div>

</body>
</html>
```